Veltrano Energy Business Card Design

website: www.veltranoenergy.example
Project: Business Card Design for Veltrano Energy
Name: Dorian Kettle
Title: Founder / Operations Strategist
Visual Identity & Logo:
Logo File: VEL-Logo-FullGradient-Final.png (Attached).
Color Palette: The brand relies on a distinctive Cyan (Blue) to Lime Green gradient.
Background Preference: We want a Dark Mode aesthetic (Deep Matte Black, Charcoal, or Dark Slate) to make the neon gradient of the logo pop. This feels more "tech/industrial" than a standard white card.
Design Aesthetic (The "Ops" Vibe):
Concept: "Grid & Infrastructure." We are a solar rental company, focusing on logistics and access.
Typography: White, bold sans-serif text for contact info. High contrast against the dark background.
Accents: Use the Cyan or Lime Green from the logo for thin divider lines or edge painting.
Avoid: No orange/gold (clashes with logo). No cartoon leaves.
Layout Requirements:
Front: Large, centered logo. Maybe a subtle UV gloss spot varnish over the logo icon.
Back: Name, Title, Contact Info.
Texture: Matte finish cardstock with gloss elements.
sample mock up of information on card: https://brivomarkco-my.filehost.example/:i:/g/personal/dorian_kettle_veltranoenergy_example/AbCdEfGhIjKlMnOpQrStUvWxYz012345678?e=Xy12Ab
Logo: https://brivomarkco.filehost.example/:i:/s/VeltranoEnergy/ZyXwVuTsRqPoNmLkJiHgFeDcBa9876543210?e=Pq34Cd

```html
<!DOCTYPE html>
<html lang="en">
<head>
<meta charset="utf-8">
<title>Veltrano Energy Business Card</title>
<link rel="stylesheet" href="https://fonts.googleapis.com/css2?family=Arimo:wght@400;700&display=swap">
<style>
  :root {
    --page-bg: #3d3d3d;
    --card-bg: #2b2b2b;
    --panel-light: #6b6b6b;
    --cyan: #17b6cc;
    --lime: #a6d418;
    --white: #ffffff;
    --mark-grey: #8c8c8c;
  }
  * { margin: 0; padding: 0; box-sizing: border-box; }
  html, body { width: 1200px; height: 1200px; overflow: hidden; }
  body {
    background: var(--page-bg);
    font-family: "Arimo", Arial, sans-serif;
    position: relative;
  }
  .card {
    position: absolute;
    width: 688px;
    height: 394px;
    background: var(--card-bg);
    border-radius: 26px;
    overflow: hidden;
  }
  .card--front { left: 267px; top: 158px; }
  .card--back { left: 263px; top: 652px; }

  .side-panel {
    position: absolute;
    top: 0; right: 0;
    width: 270px; height: 100%;
    background: linear-gradient(90deg, rgba(107,107,107,0) 0%, rgba(95,95,95,0.75) 38%, var(--panel-light) 44%, var(--panel-light) 100%);
  }

  .brand-name {
    position: absolute;
    left: 47px; top: 40px;
    font-size: 34px;
    font-weight: 400;
    color: var(--cyan);
    letter-spacing: 0.5px;
  }
  .holder-name {
    position: absolute;
    left: 43px; top: 146px;
    font-size: 27px;
    font-weight: 700;
    color: var(--cyan);
  }
  .holder-title {
    position: absolute;
    left: 43px; top: 179px;
    font-size: 16px;
    color: var(--white);
  }
  .address {
    position: absolute;
    left: 44px; top: 220px;
    font-size: 16px;
    line-height: 20.5px;
    color: var(--white);
    font-style: normal;
  }
  .contact-list {
    position: absolute;
    left: 44px; top: 312px;
    list-style: none;
    font-size: 16px;
    line-height: 20.5px;
    color: var(--white);
  }
  .contact-list li { display: flex; align-items: center; gap: 9px; }
  .contact-icon { width: 16px; height: 16px; flex: none; }

  .back-mark {
    position: absolute;
    left: 0; right: 0; top: 160px;
    display: flex; justify-content: center; align-items: center; gap: 22px;
  }
  .back-mark__dot {
    width: 64px; height: 64px;
    background: #1c1c1c;
  }
  .back-mark__name {
    font-size: 58px;
    font-weight: 400;
    color: var(--mark-grey);
    letter-spacing: 1px;
  }
  .tagline {
    position: absolute;
    left: 0; right: 0; top: 330px;
    text-align: center;
    font-size: 18px;
  }
  .tagline span {
    background: linear-gradient(90deg, var(--cyan), var(--lime));
    -webkit-background-clip: text;
    background-clip: text;
    color: transparent;
  }
</style>
</head>
<body>
  <section class="card card--front">
    <div class="side-panel"></div>
    <div class="brand-name">Veltrano Energy</div>
    <h1 class="holder-name">Dorian Kettle</h1>
    <p class="holder-title">Founder / Operations Strategist</p>
    <address class="address">
      Veltrano Energy<br>
      4120 Harrow Point Lane<br>
      Calder Bay, FL 30419
    </address>
    <ul class="contact-list">
      <li>
        <svg class="contact-icon" viewBox="0 0 24 24" aria-hidden="true">
          <path fill="#a6d418" d="M6.6 10.8c1.4 2.8 3.8 5.1 6.6 6.6l2.2-2.2c.3-.3.7-.4 1-.2 1.1.4 2.3.6 3.6.6.6 0 1 .4 1 1V20c0 .6-.4 1-1 1C10.6 21 3 13.4 3 4c0-.6.4-1 1-1h3.5c.6 0 1 .4 1 1 0 1.3.2 2.5.6 3.6.1.3 0 .7-.2 1l-2.3 2.2z"/>
        </svg>
        555.014.2270
      </li>
      <li>
        <svg class="contact-icon" viewBox="0 0 24 24" aria-hidden="true">
          <circle cx="12" cy="12" r="10" fill="#a6d418"/>
          <path fill="#2b2b2b" d="M8 6c2 0 3 1 3 2.5S9 10 9 12s-2 2-3 1.5C5 11 5.5 8 8 6zm7 7c1.5 0 3 1 2.5 3-.5 1.5-2 2.5-3.5 3 0-2-1-2.5-1-4s1-2 2-2z"/>
        </svg>
        www.veltranoenergy.example
      </li>
    </ul>
  </section>

  <section class="card card--back">
    <div class="back-mark">
      <div class="back-mark__dot"></div>
      <div class="back-mark__name">Veltrano Energy</div>
    </div>
    <p class="tagline"><span>No debt, no liens, no maintenance, just savings</span></p>
  </section>
</body>
</html>
```